■書籍タイトル
「町工房・路地の店・士業のための、明日効く集客設計術・KRT」

・堅苦しくなく、わかりやすいイメージにしたいです
・電子書籍なので、画像が小さいので、できるだけ視認しやすい文字でお願いします

■オビ
「お金も時間もかけずに、たった2つのことをするだけで、ライバルが歯ぎしりするほどお客に選ばれる」

■著者  森野沙知絵
■発行  東陽商務文化出版舎

■色の指定などはありません。お任せです。
(明るい・カンタン・わかりやすい)
イメージイラストなど入ってもよいかと思います。

■高級感やアカデミックより、明るくカンタンなイメージで。

※参考資料として、書籍の原稿と、同じタイトルのセミナーのパワポ表紙画像を添付します。
アカデミックな感じより、ポップな感じや明るいイメージ、
「わかりやすさ」「文字の視認性」を重視します。
クラフターのみなさま、
引き続き、ご提案をお待ちしております。
みなさま、ご提案ありがとうございます。

中小企業・小さなお店・先生業
という文字が小さい表示のデザインが多いのですが、

ターゲット層が一目で見てわかるよう、

中小企業・小さなお店・先生業

という文字が見えるようにしたいです。

引き続き、みなさまからのご提案をお待ちしております。
たくさんのご提案をいただきありがとうございます。

本のタイトルが、変更となりました。
金額をアップし、締め切りを1日延長いたしますので、
訂正ご対応いただければ幸いです。

新しいタイトルは、

「中小企業・小さなお店・先生業が
常連が増え続けるために明日から始める三つの習慣」
です。

帯、またはサブタイトルは、
「ライバルが歯ぎしりするほどお客が押し寄せる新時代の差別化戦略」
としてください。

ご提案をお待ちしております。
よろしくお願いいたします。

今回の装丁は、特に「わかりやすさ」を重視しておりました。
レベルの高い装丁デザインが多く、選考に大変迷いました。
選定させていただきましたデザインは、笑顔の3職種の人物のイラストと、フォントの使い方など、わかりやすい・明るい・カンタンという目指すところをこちらの想定以上に表現していただいたことが一番の理由です。

たくさんのご提案をいただき、ありがとうございました。
本当にレベルの高いデザインが多く選定では社内でも意見が割れました。
また、再三の追記・変更によりお手数をおかけしましたことを、この場を借りてお詫び申し上げます。

今後も定期的に装丁の依頼をいたしますので、どうぞよろしくお願いいたします。

```html
<!DOCTYPE html>
<html lang="ja">
<head>
<meta charset="utf-8">
<title>町工房・路地の店・士業のための、明日効く集客設計術</title>
<link href="https://fonts.googleapis.com/css2?family=Noto+Sans+JP:wght@500;700;900&family=M+PLUS+Rounded+1c:wght@800&display=swap" rel="stylesheet">
<style>
  :root {
    --yellow: #ffe100;
    --yellow-soft: #fff3a0;
    --red: #e8202a;
    --ink: #1a1a1a;
    --white: #ffffff;
  }
  * { margin: 0; padding: 0; box-sizing: border-box; }
  html, body { width: 759px; height: 1200px; overflow: hidden; }
  body { font-family: "Noto Sans JP", sans-serif; color: var(--ink); }
  .cover {
    position: relative; width: 759px; height: 1200px;
    background: var(--yellow); overflow: hidden;
  }
  .hero-art {
    position: absolute; left: 0; top: 0; width: 759px; height: 290px;
    background: linear-gradient(180deg, var(--yellow) 0%, var(--yellow-soft) 55%, var(--yellow) 100%);
  }
  .audience {
    position: absolute; left: 44px; top: 304px;
    display: flex; align-items: center; gap: 9px;
  }
  .audience-tag {
    background: var(--red); color: var(--white);
    font-weight: 900; font-size: 38px; line-height: 1;
    padding: 8px 12px; border-radius: 4px;
  }
  .audience-particle { font-weight: 900; font-size: 40px; line-height: 1; margin-left: 2px; }
  .lead {
    position: absolute; left: 180px; top: 382px;
    font-weight: 900; font-size: 40px; line-height: 1.2;
  }
  .main-title {
    position: absolute; left: 0; width: 759px; top: 470px;
    text-align: center; font-family: "M PLUS Rounded 1c", sans-serif;
    font-weight: 800; line-height: 1; white-space: nowrap;
  }
  .main-title .numeral { font-size: 190px; }
  .main-title .rest { font-size: 128px; }
  .author {
    position: absolute; left: 0; width: 759px; top: 646px;
    display: flex; justify-content: center; align-items: flex-start; gap: 10px;
  }
  .author-mark {
    width: 26px; height: 26px; margin-top: 8px;
    background: var(--ink); color: var(--yellow);
    font-size: 16px; font-weight: 700; line-height: 26px; text-align: center;
  }
  .author-name { font-weight: 700; font-size: 40px; line-height: 1; text-align: center; }
  .author-roman { display: block; font-size: 13px; font-weight: 500; margin-top: 4px; letter-spacing: 0.04em; }
  .tagline {
    position: absolute; left: 0; top: 706px; width: 759px; height: 56px;
    background: var(--ink); color: var(--white);
    font-weight: 900; font-size: 33px; line-height: 56px; text-align: center; white-space: nowrap;
  }
  .tagline em { font-style: normal; color: var(--yellow); }
  .strategy-band {
    position: absolute; left: 0; top: 762px; width: 759px; height: 438px;
    background: var(--red);
  }
  .strategy {
    position: absolute; left: 0; width: 759px; top: 58px;
    text-align: center; font-weight: 900; font-size: 132px; line-height: 1.12;
    color: var(--ink);
  }
  .publisher {
    position: absolute; left: 0; width: 759px; bottom: 22px;
    text-align: center; color: var(--white); font-weight: 700; font-size: 22px;
  }
</style>
</head>
<body>
  <main class="cover">
    <div class="hero-art" role="img" aria-label="町工房・路地の店・士業の笑顔の人物たちと白い街並みのイラスト"></div>

    <div class="audience">
      <span class="audience-tag">町工房</span>
      <span class="audience-tag">路地の店</span>
      <span class="audience-tag">士業</span>
      <span class="audience-particle">が</span>
    </div>

    <p class="lead">常連が増え続けるために<br>明日から始める</p>

    <h1 class="main-title"><span class="numeral">三</span><span class="rest">つの習慣</span></h1>

    <div class="author">
      <span class="author-mark">著</span>
      <p class="author-name">森野沙知絵<span class="author-roman">Sachie Morino</span></p>
    </div>

    <p class="tagline">ライバルが歯ぎしりするほど<em>お客が押し寄せる</em></p>

    <section class="strategy-band">
      <h2 class="strategy">明日効く<br>集客設計術</h2>
      <p class="publisher">東陽商務文化出版舎</p>
    </section>
  </main>
</body>
</html>
```